WALKING FOOD TOURISM BUSINESS. REQUEST FOR DIGITAL BROCHURE

Our business is a walking food tourism business in and around Melbourne's central city. We are needing a e-digital brochure - to be solely used as email' marketing content, not print. Therefore PDF size needs to be appropriate/suitable. Please see attached written content required for the brochure - together with our logo. For images, I am happy for designer to use our website content (www.wanderplatekitchen.com). OR any other appropriate and creative 'foodie' or Melbourne image suitable. Many thanks:)

Target Market(s)

Premium brand travellers or local adventurous Australians.

Requirements
Must have
• Quality font and images
Nice to have
• Quality Melbourne and food images. See website - wanderplatekitchen.com
Should not have
• Too much colour. Brand is black and white, sophisticated, premium product.

```html
<!DOCTYPE html>
<html lang="en">
<head>
<meta charset="utf-8">
<title>Wanderplate Kitchen Experiences – Brochure</title>
<link href="https://fonts.googleapis.com/css2?family=Poppins:wght@300;400;500&family=Roboto+Condensed:wght@400;700&display=swap" rel="stylesheet">
<style>
:root{
  --navy:#2e3348;
  --navy-deep:#23283a;
  --ink:#333846;
  --muted:#555a66;
  --paper:#ffffff;
  --paper-fade:#eceef2;
  --backdrop:#d9dadc;
}
*{box-sizing:border-box;margin:0;padding:0}
html,body{width:1200px;height:3451px;overflow:hidden}
body{background:var(--backdrop);position:relative;font-family:"Roboto Condensed",Arial,sans-serif;color:var(--ink)}
.page{position:absolute;left:197px;width:821px;height:577px;background:var(--paper);overflow:hidden;box-shadow:0 6px 14px rgba(0,0,0,.25)}
.page svg.art{position:absolute;left:0;top:0}
.bar{position:absolute;left:0;right:0;bottom:0;background:var(--navy)}
h2{font-family:"Poppins",Arial,sans-serif;font-weight:400;color:var(--ink)}

/* cover */
.cover{top:154px;background:linear-gradient(#fff 60%,#ececef)}
.cover .brand{position:absolute;left:0;right:0;top:175px;text-align:center;font-family:"Poppins",Arial,sans-serif;font-weight:400;font-size:38px;color:#fff;letter-spacing:1px}
.cover .title{position:absolute;left:0;right:0;top:470px;text-align:center;font-size:29px;font-family:"Poppins",Arial,sans-serif;font-weight:400;color:var(--ink)}
.cover .bar{height:40px;display:flex;align-items:center;justify-content:space-around;color:#fff;font-family:"Poppins",Arial,sans-serif;font-size:15px;padding:0 30px}
.cover .bar span{display:flex;align-items:center;gap:10px}

/* about */
.about{top:768px;background:linear-gradient(#fff 40%,var(--paper-fade))}
.about h2{position:absolute;left:0;right:0;top:362px;text-align:center;font-size:30px}
.about .rule{position:absolute;left:326px;width:170px;top:410px;height:2px;background:var(--ink)}
.about p{position:absolute;left:80px;right:60px;top:432px;text-align:center;font-size:12.5px;line-height:19px;color:var(--muted)}
.about .bar{height:21px}

/* experiences */
.exp{top:1398px}
.exp .col{position:absolute;left:444px;right:22px;top:14px}
.exp.right-photo .col{left:30px;right:436px;top:70px}
.exp h2{font-size:29px;margin-bottom:8px}
.tour{margin-bottom:16px}
.tour h3{display:inline-block;background:var(--navy);color:#fff;font-size:12px;font-weight:700;padding:2px 28px 2px 4px;clip-path:polygon(0 0,88% 0,100% 100%,0 100%);min-width:228px}
.tour .meta{font-size:12px;font-weight:700;color:var(--ink);margin:1px 0 2px}
.tour p{font-size:11px;line-height:13.6px;color:var(--muted);text-align:justify;margin-bottom:8px}
.exp .bar{height:18px}
</style>
</head>
<body>

<!-- Cover -->
<section class="page cover">
  <svg class="art" width="821" height="577" viewBox="0 0 821 577">
    <defs>
      <linearGradient id="lanewayTone" x1="0" y1="0" x2="0" y2="1">
        <stop offset="0" stop-color="#3a3b40"/><stop offset="1" stop-color="#1f1d1c"/>
      </linearGradient>
      <clipPath id="c1"><circle cx="258" cy="395" r="58"/></clipPath>
    </defs>
    <path role="img" aria-label="Photo of a busy Melbourne laneway with cafés at night" d="M0 0H821V360Q600 390 420 380Q200 330 0 345Z" fill="url(#lanewayTone)"/>
    <path d="M420 380Q600 392 821 365" stroke="var(--navy)" stroke-width="6" fill="none"/>
    <circle role="img" aria-label="Photo of a cheese board" cx="255" cy="394" r="58" fill="#b89c76" stroke="#fff" stroke-width="4"/>
    <circle role="img" aria-label="Photo of a plated restaurant dish" cx="408" cy="380" r="72" fill="#6d7078" stroke="#fff" stroke-width="4"/>
    <circle role="img" aria-label="Photo of a gourmet plate" cx="535" cy="394" r="58" fill="#a4553c" stroke="#fff" stroke-width="4"/>
  </svg>
  <div class="brand">Wanderplate Kitchen</div>
  <div class="title">WANDERPLATE KITCHEN EXPERIENCES</div>
  <div class="bar">
    <span><svg width="14" height="14" viewBox="0 0 14 14"><circle cx="7" cy="7" r="6" fill="none" stroke="#fff" stroke-width="1.5"/><rect x="4" y="5" width="6" height="4" fill="none" stroke="#fff"/></svg>info@wanderplatekitchen.com</span>
    <span><svg width="14" height="14" viewBox="0 0 14 14"><circle cx="7" cy="7" r="6" fill="none" stroke="#fff" stroke-width="1.5"/><path d="M5 4l1 2-1 1 2 2 1-1 2 1-1 2c-3 0-6-3-6-6z" fill="#fff"/></svg>0400 123 987</span>
    <span><svg width="14" height="14" viewBox="0 0 14 14"><circle cx="7" cy="7" r="6" fill="none" stroke="#fff" stroke-width="1.5"/><circle cx="7" cy="7" r="2.5" fill="none" stroke="#fff"/></svg>www.wanderplatekitchen.com</span>
  </div>
</section>

<!-- About -->
<section class="page about">
  <svg class="art" width="821" height="340" viewBox="0 0 821 340">
    <defs><linearGradient id="riverTone" x1="0" y1="0" x2="0" y2="1"><stop offset="0" stop-color="#7fa6cf"/><stop offset=".45" stop-color="#5d6a60"/><stop offset="1" stop-color="#2d3a3c"/></linearGradient></defs>
    <path role="img" aria-label="Photo of the Yarra River with moored boats and city bridge" d="M0 0H821V285Q600 330 410 318Q200 305 0 290Z" fill="url(#riverTone)"/>
    <path d="M0 288Q200 306 410 317Q620 328 821 282" stroke="var(--navy)" stroke-width="6" fill="none"/>
  </svg>
  <h2>About Us</h2>
  <div class="rule"></div>
  <p>We provide experiential adventure for visitors and locals alike - all through the 'lens' of exceptional food. Our tour experiences capture the essence of Melbourne, its people and diverse history - stopping to sip, savour and delight in Melbourne's foodie hot spots &amp; indulging in their signature tastes.</p>
  <div class="bar"></div>
</section>

<!-- Our Experiences -->
<section class="page exp">
  <svg class="art" width="440" height="577" viewBox="0 0 440 577">
    <defs><linearGradient id="gardenTone" x1="0" y1="0" x2="0" y2="1"><stop offset="0" stop-color="#c9c2a8"/><stop offset=".6" stop-color="#8e8a7c"/><stop offset="1" stop-color="#4f7a32"/></linearGradient></defs>
    <path role="img" aria-label="Photo of the domed Royal Exhibition Building behind autumn trees and a fountain" d="M0 0H335Q410 250 380 560H0Z" fill="url(#gardenTone)"/>
    <path d="M335 0Q440 260 395 577" stroke="var(--navy)" stroke-width="6" fill="none"/>
  </svg>
  <div class="col">
    <h2>Our Experiences</h2>
    <div class="tour">
      <h3>FOODIES BUCKET LIST TOUR</h3>
      <div class="meta">3.5 hours / A$159 Adult / A$119 Child / Up to 8 guests</div>
      <p>Think you're a foodie? Are you torn by delicious culinary choices and have a fear of missing out on the true Melbourne foodie experience? If your answers are 'yes', then our 'Bucket List' adventure is for you. When time is of the essence, our 'Bucket List Tour' will 'wow' your senses - while tasting and strolling your way through Melbourne's exploding culinary epicentre.</p>
    </div>
    <div class="tour">
      <h3>STREET EATS TOUR</h3>
      <div class="meta">3.5 hours / A$159 Adult / A$119 Child / Up to 8 guests</div>
      <p>Hungry? Then why not broaden your palette and TAKE IT TO THE STREETS - Melbourne style. Our Street Eats Tour is ideal for locals and visitors, keen to wander, explore &amp; taste Melbourne's Asian 'street food' scene. Taste your way in and around Melbourne – slurping up Thai noodles, devouring Shanghai Dumplings, Korean bites, Japanese treats and more – whilst taking in mystical immigrant stories - from the Chinese arrival, the Vietnamese and later, the sub-continent. The perfect experience to capture some of Melbourne's best, hidden treasures.</p>
    </div>
    <div class="tour">
      <h3>THE STORY OF MELBOURNE</h3>
      <div class="meta">2.5 hours / A$89 Adult / A$49 Child / Up to 12 guests</div>
      <p>From the Yarra River to Iconic Laneways, Historic Precincts, Theatres &amp; Cathedrals - discover the character, culture &amp; community of our magnificent city, that is MELBOURNE. Walk with us on tour, as we share stories about Melbourne's past and present. Along your journey you'll take in the very fabric of Melbourne. From the early beginnings – through to today, soaking in why Melbourne continues to be one of the greatest multi-cultural cities in the world.</p>
    </div>
  </div>
  <div class="bar"></div>
</section>

<!-- Evening & Private -->
<section class="page exp right-photo" style="top:2033px">
  <svg class="art" width="821" height="577" viewBox="0 0 821 577">
    <defs><linearGradient id="distilleryTone" x1="0" y1="0" x2="0" y2="1"><stop offset="0" stop-color="#9a8c80"/><stop offset=".5" stop-color="#7a5a48"/><stop offset="1" stop-color="#3f3a38"/></linearGradient></defs>
    <path role="img" aria-label="Photo of a tasting group at a distillery with copper stills" d="M445 0H821V560H420Q390 250 445 0Z" fill="url(#distilleryTone)"/>
    <path d="M445 0Q385 260 425 577" stroke="var(--navy)" stroke-width="6" fill="none"/>
  </svg>
  <div class="col">
    <div class="tour">
      <h3>EVENING PALATE &amp; PAIRING</h3>
      <div class="meta">3 hours / A$199 Adult / A$159 Child / Up to 8 guests</div>
      <p>Enjoy your evening in one of Melbourne most vibrant, mouth-watering, delectable foodie precincts. You'll be 'wowed' by Melbourne's charm and hospitality as you experience signature tastes from some of our best restaurants - pairing flavours and textures at each venue – and hearing the stories that transformed Melbourne into the marvellous 'food capital' city it is today.</p>
    </div>
    <div class="tour" style="margin-top:30px">
      <h3>PRIVATE EXPERIENCES</h3>
      <div class="meta">Up to 8 hours / Tailored itineraries</div>
      <p>Our private tours are ideal for the ultimate fun 'group adventure'. Share and experience the cultural delights of Melbourne with good friends – perhaps a team building event, a family reunion, a special birthday or wedding party. All with your very own personal tour host.</p>
      <p>Choose from one of our <b>Wanderplate Kitchen Experiences</b> – with the option to customise the tour length, start time and tour distance covered. OR tailor your own experience to suit your interest, theme, community and corporate groups.</p>
      <p>Either way, your PRIVATE EXPERIENCE will be created with you in mind.</p>
      <p>Enquiries: <b>info@wanderplatekitchen.com</b></p>
    </div>
  </div>
  <div class="bar"></div>
</section>

<!-- Back cover -->
<section class="page" style="top:2680px;background:#3a3f52">
  <svg class="art" width="821" height="577" viewBox="0 0 821 577">
    <rect role="img" aria-label="Darkened photo of a crowded street art laneway" width="821" height="577" fill="#41465a"/>
  </svg>
  <div style="position:absolute;left:0;right:0;top:245px;text-align:center;color:#fff;font-family:'Poppins',Arial,sans-serif;font-size:30px;font-weight:400">Wanderplate Kitchen</div>
  <div style="position:absolute;left:0;right:0;top:324px;text-align:center;color:#fff;font-family:'Poppins',Arial,sans-serif;font-size:28px;font-weight:300">For Booking Schedule &amp; Enquiry</div>
  <div style="position:absolute;left:264px;width:294px;top:373px;height:34px;border-radius:17px;background:#fff;color:var(--navy);font-family:'Poppins',Arial,sans-serif;font-weight:500;font-size:20px;display:flex;align-items:center;justify-content:center;gap:10px">
    <svg width="18" height="18" viewBox="0 0 18 18"><circle cx="9" cy="9" r="8" fill="none" stroke="var(--navy)" stroke-width="1.5"/><path d="M6 5l1.3 2.5-1.2 1.2 2.3 2.4 1.2-1.2 2.5 1.3-1.2 2.2C7.8 13.4 4.6 10.2 4.6 6.2z" fill="var(--navy)"/></svg>0400 123 987
  </div>
  <div style="position:absolute;left:0;right:0;top:447px;display:flex;justify-content:center;gap:22px;color:#fff;font-family:'Poppins',Arial,sans-serif;font-size:15px">
    <span style="display:flex;align-items:center;gap:8px"><i style="width:20px;height:20px;border-radius:50%;background:#fff;display:inline-block"></i>Wanderplate.Kitchen</span>
    <span style="display:flex;align-items:center;gap:8px"><i style="width:20px;height:20px;border-radius:50%;background:#fff;display:inline-block"></i>wanderplate.kitchen</span>
  </div>
  <div style="position:absolute;left:0;right:0;top:502px;text-align:center;color:#fff;font-size:12px">CANCELLATION &amp; AMENDMENTS</div>
  <div style="position:absolute;left:0;right:0;top:527px;text-align:center;color:#fff;font-size:10.5px">100% REFUND for cancellations outside 24 hours of the tour departure time &nbsp;|&nbsp; NO REFUND for cancellations made within 24 hours of the tour departure time</div>
</section>

</body>
</html>
```